Vostrel LTB Book Cover Design: Book 1 of 4

Designers must not submit more than 1 design. Submission of multiple designs will result in disqualification.

Designer must be highly experienced with properly designing and formatting Vostrel LTB book covers. The winner of this contest will receive three more covers to do. This project is for one of four books in a series. I want the same designer to do all four books because they are in a series and need to look the same. Attached are the directions and files.

Target Market(s)

see attachments

Industry/Entity Type

see attachments

Requirements
Must have
• see attachments
Nice to have
• see attachments
Should not have
• see attachments

```html
<!DOCTYPE html>
<html lang="en">
<head>
<meta charset="utf-8">
<title>Know The Hull – Book Cover</title>
<link rel="stylesheet" href="https://fonts.googleapis.com/css2?family=Bebas+Neue&family=Oswald:wght@400;500&family=Inter:wght@400;500;600;700&display=swap">
<style>
  :root{
    --navy:#0b111b;
    --navy-soft:#111a28;
    --gold:#b39a74;
    --white:#ffffff;
    --body:#e7e9ee;
    --sea-top:#0d4a86;
    --sea-mid:#1466a8;
    --sea-low:#0f4c8a;
  }
  *{margin:0;padding:0;box-sizing:border-box}
  html,body{width:1200px;height:844px;overflow:hidden;background:var(--navy)}
  .cover{position:relative;width:1200px;height:844px;background:var(--navy);font-family:"Inter",sans-serif;color:var(--white)}
  .display{font-family:"Bebas Neue",sans-serif;font-weight:400;letter-spacing:.5px}
  .gold{color:var(--gold)}

  /* Back */
  .back{position:absolute;left:0;top:0;width:557px;height:844px}
  .back-tagline{position:absolute;top:46px;left:0;width:557px;text-align:center;font-size:13px;line-height:18px;letter-spacing:.2px}
  .dash{display:inline-block;width:19px;height:1px;background:var(--gold);vertical-align:middle;margin:0 8px}
  .back-title{position:absolute;top:92px;left:0;width:557px;text-align:center;font-size:54px;line-height:56px}
  .back-copy{position:absolute;left:32px;width:502px;font-size:10.5px;line-height:16.8px;color:var(--body)}
  .back-copy h3{font-size:12.5px;font-weight:600;color:var(--gold);margin-bottom:6px}
  .back-copy p{margin-bottom:5px}
  .back-copy ul{list-style:none;margin-top:2px}
  .back-copy li{line-height:18.3px}
  .about h3{font-size:13.5px}
  .about p{text-align:justify}

  /* Spine */
  .spine{position:absolute;left:557px;top:0;width:89px;height:844px;background:var(--navy-soft)}
  .spine-title{position:absolute;left:30px;top:24px;writing-mode:vertical-rl;font-size:30px;line-height:30px}
  .spine-wheel{position:absolute;left:24px;top:532px}
  .spine-author{position:absolute;left:41px;top:584px;writing-mode:vertical-rl;font-size:26px;line-height:26px;white-space:nowrap}
  .spine-creds{position:absolute;left:24px;top:598px;writing-mode:vertical-rl;font-family:"Oswald",sans-serif;font-size:9.3px;line-height:10px;white-space:nowrap;color:var(--body)}

  /* Front */
  .front{position:absolute;left:646px;top:0;width:554px;height:844px}
  .front-photo{position:absolute;left:0;top:0;width:554px;height:720px;
    background:linear-gradient(180deg,var(--sea-top) 0%,#175f9f 30%,#3d79ad 36%,var(--sea-mid) 40%,var(--sea-low) 75%,#0c3f74 100%)}
  .front-tagline{position:absolute;top:38px;left:0;width:554px;text-align:center;font-size:13px;font-weight:600;line-height:17px}
  .front-title{position:absolute;top:76px;left:0;width:554px;text-align:center;font-size:100px;line-height:90px}
  .front-title-2{position:absolute;top:165px;left:0;width:554px;text-align:center;font-size:100px;line-height:90px}
  .anchor{position:absolute;left:35px;top:176px}
  .guide-note{position:absolute;left:35px;top:234px;font-size:10.6px;font-weight:700;line-height:13.6px}
  .badge{position:absolute;left:390px;top:195px;width:141px;height:141px;border-radius:50%;background:var(--navy);border:1px solid var(--gold);text-align:center}
  .badge-text{position:absolute;top:48px;left:0;width:139px;font-size:10px;font-weight:500;line-height:15px}
  .badge-rule{position:absolute;top:115px;left:49px;width:41px;height:1px;background:var(--gold)}
  .badge-compass{position:absolute;top:10px;left:33px}
  .features{position:absolute;left:27px;top:317px;list-style:none}
  .feature{position:absolute;left:0;width:360px;height:58px}
  .feature-icon{position:absolute;left:0;top:0;width:58px;height:58px;border-radius:50%;background:var(--gold);display:flex;align-items:center;justify-content:center}
  .feature-text{position:absolute;left:77px;font-size:13px;font-weight:700;line-height:17px}
  .front-band{position:absolute;left:0;top:720px;width:554px;height:124px;background:var(--navy)}
  .band-rule{position:absolute;left:26px;top:0;width:501px;height:1px;background:var(--gold)}
  .band-wheel{position:absolute;left:254px;top:-23px}
  .front-author{position:absolute;left:0;top:34px;width:554px;text-align:center;font-size:44px;line-height:44px}
  .front-creds{position:absolute;left:0;top:83px;width:554px;text-align:center;font-family:"Oswald",sans-serif;font-size:15.5px;letter-spacing:-.3px;line-height:20px}
</style>
</head>
<body>
<main class="cover">

  <section class="back">
    <p class="back-tagline"><span class="dash"></span>THE SMART BUYER’S GUIDE TO FINDING<span class="dash"></span><br>THE RIGHT BOAT AND BOATING WITH CONFIDENCE</p>
    <h1 class="back-title display">KNOW THE HULL</h1>

    <div class="back-copy" style="top:168px">
      <h3>Know The Hull:</h3>
      <p>Before you spend thousands on a boat… spend a few hours learning what experienced boaters wish they knew</p>
      <p>Buying a recreational boat is exciting—but it can also be expensive, confusing, and full of costly mistakes.</p>
      <p>This practical guide helps first-time buyers understand how to evaluate boats, compare ownership options, recognize hidden costs, and avoid expensive surprises before signing the paperwork. Through easy-to-follow explanations, checklists, comparison tables, and illustrations, you'll gain the confidence to make informed decisions and purchase a boat that truly fits your lifestyle.</p>
      <p>Whether you're shopping for your first boat or upgrading to your next one, this book will help you buy smarter and avoid the mistakes that many owners only discover after it's too late.</p>
    </div>

    <div class="back-copy" style="top:396px">
      <h3 style="font-size:11px;font-weight:500">You'll Learn How To:</h3>
      <ul>
        <li>• Choose the right boat</li>
        <li>• Compare ownership options</li>
        <li>• Inspect boats with confidence</li>
        <li>• Understand engines and systems</li>
        <li>• Estimate ownership costs</li>
        <li>• Avoid common buying mistakes</li>
        <li>• Know when to hire a surveyor</li>
        <li>• Negotiate from an informed position</li>
      </ul>
    </div>

    <div class="back-copy about" style="top:582px">
      <h3>About the Author</h3>
      <p>Captain Dorian K. Halvek is a U.S. Coast Guard Licensed Captain, certified boating instructor, military veteran, and experienced recreational boater. Having trained thousands of students and delivered hundreds of vessels, he created the Ahead of Tide series to help new boaters avoid costly mistakes and enjoy safer, more rewarding time on the water.</p>
    </div>

    <div class="back-copy about" style="top:691px">
      <h3>Series Tagline</h3>
      <p style="text-align:left">The Ahead of Tide Series<br>Helping new recreational boaters make smarter decisions before buying, boating, and traveling</p>
    </div>
  </section>

  <section class="spine">
    <h2 class="spine-title display">KNOW THE HULL</h2>
    <svg class="spine-wheel" width="40" height="40" viewBox="0 0 40 40" fill="none" stroke="var(--gold)" stroke-width="2.2">
      <circle cx="20" cy="20" r="11"/><circle cx="20" cy="20" r="3.5"/>
      <path d="M20 2v36M2 20h36M7.3 7.3l25.4 25.4M32.7 7.3L7.3 32.7"/>
    </svg>
    <p class="spine-author display">BY CAPTAIN DORIAN K. HALVEK</p>
    <p class="spine-creds">USCG-LICENSED CAPTAIN . CERTIFIED BOATING INSTRUCTOR . VETERAN</p>
  </section>

  <section class="front">
    <div class="front-photo" role="img" aria-label="Aerial photograph of a cable-stayed bridge crossing blue open water under a clear sky"></div>

    <p class="front-tagline"><span class="dash" style="background:var(--white)"></span>THE SMART BUYER’S GUIDE TO FINDING<span class="dash" style="background:var(--white)"></span><br>THE RIGHT BOAT AND BOATING WITH CONFIDENCE</p>
    <h1 class="front-title display">KNOW THE</h1>
    <p class="front-title-2 display">HULL</p>

    <svg class="anchor" width="116" height="52" viewBox="0 0 116 52" fill="none" stroke="var(--white)" stroke-width="3" stroke-linecap="round">
      <path d="M1 38h17M98 38h17"/>
      <circle cx="58" cy="6" r="4"/>
      <path d="M58 10v38M50 17h16M40 32c2 10 10 15 18 16c8-1 16-6 18-16"/>
      <path d="M36 30l4 2 2-4M80 30l-4 2-2-4"/>
    </svg>
    <p class="guide-note">A COMPLETE GUIDE FOR<br>FIRST TIME BOAT BUYERS<br>FROM SHOPING TO SEA<br>TRIAL AND BEYOND</p>

    <div class="badge">
      <svg class="badge-compass" width="74" height="28" viewBox="0 0 74 28" fill="none" stroke="var(--gold)" stroke-width="1.6">
        <path d="M0 14h14M60 14h14"/>
        <circle cx="37" cy="14" r="12"/>
        <path d="M42 9l-3 7-7 3 3-7z"/>
      </svg>
      <p class="badge-text">AVOID COSTLY<br>MISTAKES<br>BUY WITH<br><span class="gold">CONFIDENCE</span></p>
      <span class="badge-rule"></span>
    </div>

    <ul class="features">
      <li class="feature" style="top:0">
        <span class="feature-icon"><svg width="30" height="30" viewBox="0 0 30 30" fill="none" stroke="#fff" stroke-width="2.6" stroke-linecap="round"><circle cx="12" cy="12" r="8"/><path d="M18 18l9 9"/></svg></span>
        <span class="feature-text" style="top:5px">FIND THE RIGHT BOAT<br>FOR YOUR NEEDS<br>AND BUDGET</span>
      </li>
      <li class="feature" style="top:74px">
        <span class="feature-icon"><svg width="30" height="30" viewBox="0 0 30 30" fill="none" stroke="#fff" stroke-width="2.2" stroke-linecap="round"><circle cx="15" cy="15" r="12"/><path d="M9 15l5 5 11-14"/></svg></span>
        <span class="feature-text" style="top:5px">SHOP SMART<br>AND AVOID<br>RED FLAGS</span>
      </li>
      <li class="feature" style="top:147px">
        <span class="feature-icon"><svg width="30" height="30" viewBox="0 0 30 30" fill="#fff"><path d="M15 2L8 22h7zM17 6l7 16h-7z"/><path d="M4 24h22l-3 4H7z"/></svg></span>
        <span class="feature-text" style="top:14px">SEA TRIAL<br>LIKE A PRO</span>
      </li>
      <li class="feature" style="top:218px">
        <span class="feature-icon"><svg width="26" height="30" viewBox="0 0 26 30" fill="none" stroke="#fff" stroke-width="1.6"><rect x="3" y="4" width="20" height="24" rx="2"/><rect x="8" y="2" width="10" height="4" rx="1"/><path d="M7 13h3M12 13h8M7 18h3M12 18h8M7 23h8"/></svg></span>
        <span class="feature-text" style="top:5px">INSPECTIONS,<br>SURVEY &amp;<br>NEGOTIATIONS</span>
      </li>
      <li class="feature" style="top:292px">
        <span class="feature-icon"><span style="font-weight:700;font-size:32px;color:#fff;line-height:1">$</span></span>
        <span class="feature-text" style="top:5px">UNDERSTAND<br>TRUE OWNERSHIP<br>COST</span>
      </li>
    </ul>

    <div class="front-band">
      <span class="band-rule"></span>
      <svg class="band-wheel" width="46" height="46" viewBox="0 0 40 40" fill="none" stroke="var(--gold)" stroke-width="2.2">
        <circle cx="20" cy="20" r="11"/><circle cx="20" cy="20" r="3.5"/>
        <path d="M20 2v36M2 20h36M7.3 7.3l25.4 25.4M32.7 7.3L7.3 32.7"/>
      </svg>
      <p class="front-author display">BY CAPTAIN DORIAN K. HALVEK</p>
      <p class="front-creds">USCG-LICENSED CAPTAIN . CERTIFIED BOATING INSTRUCTOR . VETERAN</p>
    </div>
  </section>

</main>
</body>
</html>
```